4 Widows HAUNTED Beyond Dusk (A household sinking under ancient vows)

I want my book cover to coincide with the title. The "T" In Birth I want to be a cross with God on it. I want some of the letters melting. I also want a pit or a pool of fire with 9 fiery sisters drowning in it. It doesn't necessarily have to show the complete body, it can partial, some full, and some with just the hands coming out the fire like they have already drowned. The color of the cover I rather have it black since the fire is reddish, yellow/orange; but I'm open to creativity. My book should look like the place "Hell" since that's what my non-fiction book is all about. It's a true story of a struggling family living the hard knock life in New York with a vulnerable mother without our father in our lives. We experienced living in and out of shelter, getting picked on everywhere we went, school dropouts, young teen pregnancies, victims of rape, abuse, drug use, had a lot of witchcraft interventions as well as some of us giving our lives to the devil. As we gotten old we became more evil, indulged in the 7 deadly sins was their daily routine which caused tragedies to the family and others, our family values is no longer valued, and we grew apart as a whole. So my book is delivering a message to all families who has similar stories. Inspirational to whoever is seeking guidance and understanding as well as a wake up call to struggling family, evildoers, and people who are trying to transition.. Also, I want to bring families back together; most definitely mine because we all have some sort of Envy, Greed, Lust, Rage, Sloth, Gluttony, Self-Pride, etc. Giving this brief description of my book, the cover should reveal strictly evil. No smiles, just sinful. On the back of my cover I will have a short description of my book, and telling a little about myself, so I can have a little fire on it to blend in with the front, but it's optional. I'm also open to creative ideas, so if you can make a cover through your experience that goes with my title, I am willing to see them. My book is already done and is waiting to be published so the cover is the only thing I am waiting on. I hope this information is helpful, and I'm hoping I can get a book cover I am looking for.

Font styles to use
Other font styles liked:
• I'm undecided

Colors

Designer to choose colors to be used in the design.

Requirements
Must have
• more than one person on the cover
Nice to have
• 9 fiery sisters drowning in a pool or pit of fire
Should not have
• one person on the cover

```html
<!DOCTYPE html>
<html lang="en">
<head>
<meta charset="utf-8">
<title>4 Widows HAUNTED Beyond Dusk — Cover</title>
<link rel="stylesheet" href="https://fonts.googleapis.com/css2?family=Archivo+Black&display=swap">
<style>
  :root {
    --night: #000000;
    --title-white: #ffffff;
    --title-edge: #8a8a8a;
    --tagline: #f4dc9e;
    --tagline-glow: rgba(255, 214, 140, 0.55);
    --fire-hot: #ffd27a;
    --fire-mid: #f08a2a;
    --fire-deep: #a8300e;
    --rock-light: #5a4e47;
    --rock-dark: #1c1714;
    --wood-light: #a8744a;
    --wood-dark: #4b2a14;
  }
  * { margin: 0; padding: 0; box-sizing: border-box; }
  html, body {
    width: 927px; height: 1200px; overflow: hidden;
    background: var(--night);
  }
  .cover {
    position: relative;
    width: 927px; height: 1200px;
    background: var(--night);
    overflow: hidden;
    font-family: "Archivo Black", "Arial Black", sans-serif;
  }
  .title {
    position: absolute; left: 0; top: 0; width: 100%;
    color: var(--title-white);
    font-weight: 400;
    line-height: 1;
    letter-spacing: -1px;
  }
  .title-line {
    position: absolute;
    font-size: 88px;
    white-space: nowrap;
    text-shadow:
      0 1px 0 #d9d9d9,
      0 2px 0 #bdbdbd,
      2px 3px 0 var(--title-edge),
      3px 5px 4px rgba(0,0,0,0.6),
      0 0 10px rgba(255,255,255,0.35);
  }
  .title-line--first  { left: 64px;  top: 48px; }
  .title-line--second { left: 64px;  top: 160px; }
  .title-line--third  { left: 132px; top: 272px; }
  .cross-letter {
    display: inline-block;
    vertical-align: bottom;
    width: 78px; height: 150px;
    margin: 0 2px -8px;
    border-radius: 6px;
    background: linear-gradient(160deg, var(--wood-light), var(--wood-dark));
    box-shadow: 0 0 18px rgba(255,255,255,0.45);
  }
  .visually-hidden {
    position: absolute; width: 1px; height: 1px;
    overflow: hidden; clip: rect(0 0 0 0);
  }
  .tagline {
    position: absolute; left: 264px; top: 512px;
    color: var(--tagline);
    font-size: 31px;
    line-height: 38px;
    letter-spacing: 0.5px;
    text-shadow: 0 0 8px var(--tagline-glow), 1px 2px 2px rgba(0,0,0,0.8);
  }
  .scene {
    position: absolute; left: 0; top: 656px;
    width: 927px; height: 544px;
  }
</style>
</head>
<body>
  <main class="cover">
    <h1 class="title">
      <span class="title-line title-line--first">4 Widows</span>
      <span class="title-line title-line--second">HAUNTED</span>
      <span class="title-line title-line--third">Beyond Du<span class="visually-hidden">s</span><span class="cross-letter" role="img" aria-label="carved wooden cross standing in for the letter s"></span>k</span>
    </h1>

    <p class="tagline">A household sinking<br>under ancient vows</p>

    <svg class="scene" viewBox="0 0 927 544" role="img"
         aria-label="pool of fire with several figures sinking and raising their hands, edged by dark volcanic rock">
      <defs>
        <linearGradient id="fireGlow" x1="0" y1="0" x2="0" y2="1">
          <stop offset="0" stop-color="var(--fire-deep)"/>
          <stop offset="0.3" stop-color="var(--fire-mid)"/>
          <stop offset="0.55" stop-color="var(--fire-hot)"/>
          <stop offset="0.8" stop-color="var(--fire-mid)"/>
          <stop offset="1" stop-color="var(--fire-deep)"/>
        </linearGradient>
        <linearGradient id="rockFill" x1="0" y1="0" x2="0" y2="1">
          <stop offset="0" stop-color="var(--rock-light)"/>
          <stop offset="1" stop-color="var(--rock-dark)"/>
        </linearGradient>
      </defs>
      <path class="fire-pool" fill="url(#fireGlow)"
        d="M0 90 L40 82 L90 76 L140 70 L200 72 L250 66 L300 60 L340 68 L380 58 L420 62 L470 56 L520 60 L560 40 L580 8 L600 30 L640 26 L680 44 L720 40 L760 50 L800 46 L850 56 L890 52 L927 64 L927 420 L0 420 Z"/>
      <path class="rock-rim" fill="url(#rockFill)"
        d="M0 256 L60 262 L120 280 L180 300 L240 318 L300 332 L360 342 L420 350 L480 352 L540 348 L600 340 L660 326 L720 306 L780 284 L840 266 L890 258 L927 252 L927 544 L0 544 Z"/>
    </svg>
  </main>
</body>
</html>
```